Brightpath Dental Studio

Please go to www.brightpathdentalstudio.example and obtain the current company logo.
Doctors name are
Marita Velbonne, DDS
Denis Kalb, DMD
Addresses are
318 Larchmont Ave
Teaneck, NJ 07666
201-555-0147
And
872 14th St.
West New York, NJ 07093
201-555-0182
Theme of the business card should feel modrrn and similar to the website.
Front side should include company logo, doctors name, addresses, phone numbers.
Back of the card should include blank lines for patient's name. Date and time for next scheduled appointment. And notice of 24-hr cancellation courtesy policy.
Dental

```html
<!DOCTYPE html>
<html lang="en">
<head>
<meta charset="UTF-8">
<title>Brightpath Dental Studio – Business Card</title>
<link rel="stylesheet" href="https://fonts.googleapis.com/css2?family=Open+Sans:wght@400;600;700&family=Courgette&family=Lora:wght@500&display=swap">
<style>
  :root {
    --page-bg: #e6e6e8;
    --card-bg: #ffffff;
    --card-shade: #f1f1f3;
    --navy: #2b2f6e;
    --ink: #55585e;
    --muted: #7c7f86;
    --dots: #55585e;
    --brand-dot: #b9bcc3;
  }
  * { box-sizing: border-box; margin: 0; padding: 0; }
  html, body {
    width: 1200px; height: 1200px; overflow: hidden;
    background: var(--page-bg);
    font-family: "Open Sans", sans-serif;
    color: var(--ink);
  }
  .sheet {
    width: 1200px; height: 1200px;
    display: flex; flex-direction: column;
    align-items: center; justify-content: center;
    gap: 64px;
  }
  .card {
    position: relative;
    width: 900px; height: 514px;
    background: linear-gradient(135deg, var(--card-bg) 55%, var(--card-shade));
    box-shadow: 0 6px 18px rgba(0,0,0,0.12);
    overflow: hidden;
  }
  .brand {
    display: flex; align-items: center; gap: 14px;
  }
  .brand-dot {
    width: 34px; height: 34px; border-radius: 50%;
    border: 3px solid var(--brand-dot);
  }
  .brand-name {
    font-family: "Open Sans", sans-serif;
    font-weight: 700; font-size: 34px;
    color: #2a2a2e; letter-spacing: 0.5px;
  }

  /* Front */
  .card-front .brand { position: absolute; left: 60px; top: 48px; }
  .website {
    position: absolute; left: 60px; top: 104px;
    font-size: 19px; color: var(--muted);
  }
  .doctor {
    position: absolute; left: 60px; top: 146px;
    font-family: "Courgette", cursive;
    font-size: 38px; color: var(--navy);
  }
  .credentials {
    position: absolute; left: 60px; top: 202px;
    font-size: 19px; color: var(--muted);
  }
  .contacts {
    position: absolute; left: 60px; top: 250px;
    list-style: none;
    display: flex; flex-direction: column; gap: 12px;
    font-size: 21px; color: var(--ink);
  }
  .contacts li { display: flex; align-items: center; gap: 12px; }
  .contacts svg { width: 20px; height: 20px; fill: var(--navy); flex: none; }

  /* Back */
  .card-back .brand { position: absolute; right: 56px; top: 44px; }
  .back-title {
    position: absolute; left: 60px; top: 46px;
    font-family: "Courgette", cursive;
    font-size: 36px; color: var(--navy);
  }
  .field {
    position: absolute; display: flex; align-items: flex-end; gap: 10px;
    font-size: 21px; color: var(--ink);
  }
  .field .line {
    flex: 1; height: 2px; margin-bottom: 6px;
    border-bottom: 3px dotted var(--dots);
  }
  .field-name { left: 60px; top: 130px; width: 780px; }
  .field-date-1 { left: 60px; top: 210px; width: 420px; }
  .field-time-1 { left: 510px; top: 210px; width: 330px; }
  .field-date-2 { left: 60px; top: 290px; width: 420px; }
  .field-time-2 { left: 510px; top: 290px; width: 330px; }
  .policy {
    position: absolute; left: 60px; top: 390px;
    font-family: "Lora", serif; font-weight: 500;
    font-size: 27px; color: var(--navy);
  }
</style>
</head>
<body>
<main class="sheet">

  <section class="card card-front" aria-label="Card front">
    <div class="brand">
      <span class="brand-dot"></span>
      <span class="brand-name">Brightpath Dental Studio</span>
    </div>
    <p class="website">www.brightpathdentalstudio.example</p>
    <h1 class="doctor">Marita Velbonne</h1>
    <p class="credentials">DDS Denis Kalb, DMD</p>
    <ul class="contacts">
      <li>
        <svg viewBox="0 0 24 24" aria-hidden="true"><path d="M6.6 10.8a15.1 15.1 0 0 0 6.6 6.6l2.2-2.2a1 1 0 0 1 1-.25 11.4 11.4 0 0 0 3.6.57 1 1 0 0 1 1 1V20a1 1 0 0 1-1 1A17 17 0 0 1 3 4a1 1 0 0 1 1-1h3.5a1 1 0 0 1 1 1c0 1.25.2 2.45.57 3.6a1 1 0 0 1-.25 1z"/></svg>
        <span>201-555-0182</span>
      </li>
      <li>
        <svg viewBox="0 0 24 24" aria-hidden="true"><path d="M12 3 2 12h3v8h5v-6h4v6h5v-8h3z"/></svg>
        <span>872 14th St., West New York, NJ 07093</span>
      </li>
      <li>
        <svg viewBox="0 0 24 24" aria-hidden="true"><path d="M6.6 10.8a15.1 15.1 0 0 0 6.6 6.6l2.2-2.2a1 1 0 0 1 1-.25 11.4 11.4 0 0 0 3.6.57 1 1 0 0 1 1 1V20a1 1 0 0 1-1 1A17 17 0 0 1 3 4a1 1 0 0 1 1-1h3.5a1 1 0 0 1 1 1c0 1.25.2 2.45.57 3.6a1 1 0 0 1-.25 1z"/></svg>
        <span>201-555-0147</span>
      </li>
      <li>
        <svg viewBox="0 0 24 24" aria-hidden="true"><path d="M12 3 2 12h3v8h5v-6h4v6h5v-8h3z"/></svg>
        <span>318 Larchmont Ave, Teaneck, NJ 07666</span>
      </li>
    </ul>
  </section>

  <section class="card card-back" aria-label="Card back">
    <h2 class="back-title">Next Appointment</h2>
    <div class="brand">
      <span class="brand-dot"></span>
      <span class="brand-name">Brightpath Dental Studio</span>
    </div>
    <div class="field field-name"><span>Patient's Name :</span><span class="line"></span></div>
    <div class="field field-date-1"><span>Date :</span><span class="line"></span></div>
    <div class="field field-time-1"><span>Time :</span><span class="line"></span></div>
    <div class="field field-date-2"><span>Date :</span><span class="line"></span></div>
    <div class="field field-time-2"><span>Time :</span><span class="line"></span></div>
    <p class="policy">Notice Of 24-hr Cancellation Courtesy Policy</p>
  </section>

</main>
</body>
</html>
```